Business Card Design with new logo

Dorian Pelleway 4172
E 118th St Casey, IL 62420
Cell: 217-555-0193
pellewayrestoration@mailvane.test

Classic Car Restoration Services Buy Sell Trade Consign

Dorian Pelleway 9698
Cell: 217-555-0193

```html
<!DOCTYPE html>
<html lang="en">
<head>
<meta charset="utf-8">
<title>Pelleway Restoration LLC – Business Card</title>
<link href="https://fonts.googleapis.com/css2?family=Arimo:wght@400;700&display=swap" rel="stylesheet">
<style>
  :root {
    --backdrop: #2a2b2f;
    --brand-red: #bb2129;
    --brand-navy: #1b2638;
    --card-white: #ffffff;
    --text-dark: #1f2430;
    --divider: #e2a3a6;
  }
  * { box-sizing: border-box; margin: 0; padding: 0; }
  html, body {
    width: 1200px; height: 800px; overflow: hidden;
    background: var(--backdrop);
    font-family: "Arimo", Arial, sans-serif;
  }
  .canvas { position: relative; width: 1200px; height: 800px; }
  .card {
    position: absolute; top: 245px;
    width: 540px; height: 309px;
    overflow: hidden;
    box-shadow: 0 18px 40px rgba(0,0,0,.45);
  }
  /* Front */
  .card-front { left: 45px; background: var(--brand-red); color: var(--card-white); }
  .front-brand {
    position: absolute; left: 0; right: 0; top: 96px;
    text-align: center;
  }
  .brand-mark {
    display: inline-block; width: 26px; height: 26px; border-radius: 50%;
    background: currentColor; margin-bottom: 12px;
  }
  .brand-name {
    display: block; font-weight: 700; font-size: 30px; letter-spacing: 1px;
    line-height: 1.1;
  }
  .brand-sub {
    display: block; font-weight: 700; font-size: 13px; letter-spacing: 6px;
    margin-top: 6px;
  }
  .front-tagline {
    position: absolute; left: 0; right: 0; bottom: 62px;
    text-align: center; font-weight: 700; font-size: 15px; letter-spacing: .2px;
  }
  /* Back */
  .card-back { left: 615px; background: var(--card-white); }
  .back-swoosh { position: absolute; inset: 0; }
  .back-brand {
    position: absolute; left: 24px; top: 112px; width: 220px;
    text-align: center; color: var(--brand-navy);
  }
  .back-brand .brand-mark { background: var(--brand-red); width: 22px; height: 22px; margin-bottom: 8px; }
  .back-brand .brand-name { font-size: 24px; }
  .back-brand .brand-sub { font-size: 11px; letter-spacing: 5px; color: var(--brand-navy); }
  .back-divider {
    position: absolute; left: 262px; top: 36px; width: 1px; height: 108px;
    background: var(--divider);
  }
  .contact {
    position: absolute; left: 280px; top: 34px; color: var(--text-dark);
    font-size: 12px; line-height: 1.4;
  }
  .contact-name { color: var(--brand-red); font-weight: 700; font-size: 15px; line-height: 1.1; }
  .contact-role { font-size: 12px; margin-bottom: 8px; }
  .contact-line { display: flex; align-items: center; gap: 6px; }
  .contact-line svg { flex: none; }
</style>
</head>
<body>
<main class="canvas">

  <section class="card card-front" aria-label="Card front">
    <div class="front-brand">
      <span class="brand-mark"></span>
      <span class="brand-name">PELLEWAY</span>
      <span class="brand-sub">RESTORATION LLC</span>
    </div>
    <p class="front-tagline">Classic Car Restoration Services Buy Sell Trade Consign</p>
  </section>

  <section class="card card-back" aria-label="Card back">
    <svg class="back-swoosh" width="540" height="309" viewBox="0 0 540 309" aria-hidden="true">
      <path d="M0 294 C 220 294, 390 252, 540 176 L540 309 L0 309 Z" fill="var(--brand-red)"/>
      <path d="M0 280 C 220 280, 386 236, 540 158" fill="none" stroke="var(--brand-navy)" stroke-width="6"/>
    </svg>

    <div class="back-brand">
      <span class="brand-mark"></span>
      <span class="brand-name">PELLEWAY</span>
      <span class="brand-sub">RESTORATION LLC</span>
    </div>

    <div class="back-divider"></div>

    <div class="contact">
      <p class="contact-name">MARLO FINCH</p>
      <p class="contact-role">Marketing Officer</p>
      <p>Dorian Pelleway 4172</p>
      <p>E 118th St Casey, IL 62420</p>
      <p class="contact-line">
        <svg width="11" height="11" viewBox="0 0 11 11"><rect x="2" y="0.5" width="7" height="10" rx="1.2" fill="none" stroke="var(--brand-red)" stroke-width="1.2"/></svg>
        217-555-0193
      </p>
      <p class="contact-line">
        <svg width="11" height="11" viewBox="0 0 11 11"><rect x="0" y="2" width="11" height="8" fill="var(--brand-red)"/><path d="M0 2 L5.5 6.5 L11 2" fill="none" stroke="#fff" stroke-width="1"/></svg>
        pellewayrestoration@mailvane.test
      </p>
    </div>
  </section>

</main>
</body>
</html>
```